Printing Business Card

I would like the colorful accents of my business to match with an artistic design. The idea is that I would like to have a creative mix so that I am making a embossed, suede card to show off with marketing events.

```html
<!DOCTYPE html>
<html lang="en">
<head>
<meta charset="utf-8">
<title>Keystone Print Co. — Business Card</title>
<link rel="stylesheet" href="https://fonts.googleapis.com/css2?family=Open+Sans:wght@400;700&display=swap">
<style>
  :root {
    --backdrop: #e4e7ec;
    --card: #f3f3f1;
    --ink: #2b2b2b;
    --cyan: #2aa7e2;
    --magenta: #e6397f;
    --yellow: #f2b92a;
    --black: #232323;
    --foil-light: #b9dcf7;
    --foil-mid: #4f86db;
    --foil-deep: #1b1fa0;
  }
  * { margin: 0; padding: 0; box-sizing: border-box; }
  html, body {
    width: 1200px; height: 1200px; overflow: hidden;
    background: var(--backdrop);
    font-family: "Open Sans", Arial, sans-serif;
  }
  .canvas {
    width: 1200px; height: 1200px;
    display: flex; align-items: center; justify-content: center;
  }
  .business-card {
    position: relative;
    width: 1050px; height: 600px;
    background: var(--card);
    box-shadow: 0 18px 50px rgba(40, 50, 70, 0.18);
    overflow: hidden;
  }
  .cmyk-edge {
    position: absolute; left: 0; top: 0;
    width: 40px; height: 100%;
    display: flex; flex-direction: column;
  }
  .cmyk-edge span { flex: 1; }
  .cmyk-edge .cyan { background: var(--cyan); }
  .cmyk-edge .magenta { background: var(--magenta); }
  .cmyk-edge .yellow { background: var(--yellow); }
  .cmyk-edge .black { background: var(--black); }

  .brand {
    position: absolute; left: 120px; top: 250px;
    width: 340px;
    display: flex; align-items: center; gap: 20px;
  }
  .brand-dot {
    flex: none;
    width: 54px; height: 54px; border-radius: 50%;
    background: var(--black);
  }
  .brand-name {
    font-size: 38px; font-weight: 700; color: var(--ink);
    line-height: 1.1;
  }
  .brand-name span { display: block; white-space: nowrap; }

  .contact {
    position: absolute; left: 520px; top: 165px;
    color: var(--ink); font-size: 26px; line-height: 1.36;
    font-style: normal;
    white-space: nowrap;
  }
  .contact .phone { font-weight: 700; }
  .contact .online { margin-top: 30px; }

  .foil-bar {
    position: absolute; right: 100px; top: 28px;
    width: 34px; height: 430px;
    background: linear-gradient(170deg, var(--foil-light) 0%, var(--foil-mid) 45%, var(--foil-deep) 100%);
  }
</style>
</head>
<body>
  <main class="canvas">
    <article class="business-card">
      <div class="cmyk-edge" aria-hidden="true">
        <span class="cyan"></span>
        <span class="magenta"></span>
        <span class="yellow"></span>
        <span class="black"></span>
      </div>

      <div class="brand">
        <span class="brand-dot" aria-hidden="true"></span>
        <span class="brand-name"><span>Keystone</span><span>Print Co.</span></span>
      </div>

      <address class="contact">
        <div class="street">1480 Harbor Lane</div>
        <div class="city">CA 90412</div>
        <div class="phone">(555) 214-3090</div>
        <div class="online">
          <div class="email">hello@keystoneprint.com</div>
          <div class="web">www.keystoneprint.com</div>
        </div>
      </address>

      <div class="foil-bar" aria-hidden="true"></div>
    </article>
  </main>
</body>
</html>
```